Forest Consultant/Timber Buyer needs a clean business card

We are a forestry consulting and timber buying company. We meet with private landowners and assist them with timber management and timber harvesting. We would like a professional business card, please no clip art. logo is blue and white but would like to see a gray,silver, or some other color incorporated. Would like basic contact info. Would like to the layout to be creative and sleek but masculine.

Target Market(s)

private landowners

Industry/Entity Type

Business

Contact Information for Business Card

name,position, cell number, office number, email, website. This might be to cluttered. Basic contact info is what we are looking for.

Contact info can all be on one side with logo on the other.

Font styles to use
Serif
Sans Serif

Colors
0255a3
ffffff
aaaaaa

Requirements
Must have
• We just want it professional.
Nice to have
• Creative layout.
Should not have
• please no clip art of log trucks etc.

```html
<!DOCTYPE html>
<html lang="en">
<head>
<meta charset="utf-8">
<title>Northfield Land &amp; Timber – Business Card</title>
<link rel="stylesheet" href="https://fonts.googleapis.com/css2?family=Noto+Sans:wght@400;700&family=Saira+Semi+Condensed:wght@600&display=swap">
<style>
  :root {
    --brand-blue: #0255a3;
    --deep-blue: #0e4f96;
    --white: #ffffff;
    --silver: #aaaaaa;
    --stone: #6b6b6b;
    --ink: #555555;
    --backdrop: #a9a7a8;
    --paper: #fbfbfb;
  }
  * { margin: 0; padding: 0; box-sizing: border-box; }
  html, body { width: 1200px; height: 1200px; overflow: hidden; }
  body {
    background: var(--backdrop);
    font-family: "Noto Sans", Arial, sans-serif;
    position: relative;
  }
  .card {
    position: absolute;
    width: 713px;
    overflow: hidden;
  }
  /* Front side */
  .card--front {
    left: 238px; top: 116px; height: 421px;
    background: var(--deep-blue);
  }
  .card--front .backdrop-art {
    position: absolute; left: 190px; top: 26px; width: 340px; height: 395px;
    background: linear-gradient(90deg, rgba(255,255,255,0) 0%, rgba(255,255,255,0.08) 50%, rgba(255,255,255,0) 100%);
  }
  .brand {
    position: absolute;
    display: flex; align-items: center; gap: 20px;
    font-family: "Noto Sans", Arial, sans-serif;
    font-weight: 700;
  }
  .brand__mark {
    border-radius: 50%;
    flex: none;
  }
  .brand__name { display: flex; flex-direction: column; line-height: 1; }
  .brand__main { letter-spacing: 2px; }
  .brand__sub { letter-spacing: 5px; margin-top: 10px; align-self: flex-end; }

  .card--front .brand { left: 104px; top: 141px; color: var(--white); }
  .card--front .brand__mark { width: 138px; height: 138px; border: 6px solid var(--white); }
  .card--front .brand__main { font-size: 46px; }
  .card--front .brand__sub { font-size: 17px; }

  /* Back side */
  .card--back {
    left: 229px; top: 644px; height: 418px;
    background: var(--paper);
  }
  .side-band {
    position: absolute; left: 0; top: 0; bottom: 0; width: 67px;
    background: var(--deep-blue);
    border-right: 7px solid var(--stone);
  }
  .card--back .backdrop-art {
    position: absolute; left: 540px; top: 0; width: 173px; height: 418px;
    background: linear-gradient(90deg, rgba(170,170,170,0) 0%, rgba(170,170,170,0.18) 60%, rgba(170,170,170,0.22) 100%);
  }
  .card--back .brand { left: 318px; top: 30px; color: var(--brand-blue); gap: 18px; }
  .card--back .brand__mark { width: 100px; height: 100px; border: 5px solid var(--brand-blue); }
  .card--back .brand__main { font-size: 34px; }
  .card--back .brand__sub { font-size: 14px; letter-spacing: 4px; margin-top: 8px; }

  .holder { position: absolute; left: 104px; top: 188px; }
  .holder__name {
    font-family: "Saira Semi Condensed", "Arial Narrow", sans-serif;
    font-weight: 600; font-size: 28px; color: var(--ink); line-height: 1.2;
  }
  .holder__title { font-size: 16px; color: var(--stone); margin-top: 4px; }

  .contact { position: absolute; left: 104px; top: 276px; list-style: none; color: var(--stone); font-size: 17px; }
  .contact__item { display: flex; align-items: center; height: 27px; }
  .contact__icon { width: 18px; height: 18px; margin-right: 18px; fill: var(--brand-blue); }
  .contact__address { margin-top: 6px; }
</style>
</head>
<body>
  <section class="card card--front" aria-label="Card front">
    <div class="backdrop-art" role="img" aria-label="Faint evergreen tree silhouette in the background"></div>
    <div class="brand">
      <span class="brand__mark"></span>
      <span class="brand__name">
        <span class="brand__main">NORTHFIELD</span>
        <span class="brand__sub">LAND &amp; TIMBER</span>
      </span>
    </div>
  </section>

  <section class="card card--back" aria-label="Card back">
    <div class="side-band"></div>
    <div class="backdrop-art" role="img" aria-label="Faint grey evergreen tree silhouette at the right edge"></div>
    <div class="brand">
      <span class="brand__mark"></span>
      <span class="brand__name">
        <span class="brand__main">NORTHFIELD</span>
        <span class="brand__sub">LAND &amp; TIMBER</span>
      </span>
    </div>

    <div class="holder">
      <p class="holder__name">Your Good Name</p>
      <p class="holder__title">Your Title</p>
    </div>

    <ul class="contact">
      <li class="contact__item">
        <svg class="contact__icon" viewBox="0 0 20 20"><path d="M2 6c0-2 3-3 8-3s8 1 8 3v2h-4V6H6v2H2z"/><path d="M4 9h12l2 8H2z"/><circle cx="10" cy="13" r="2.2" fill="#fbfbfb"/></svg>
        +00 111 222 3333
      </li>
      <li class="contact__item">
        <svg class="contact__icon" viewBox="0 0 20 20"><path d="M1 4h18v12H1z"/><path d="M1 4l9 7 9-7" fill="none" stroke="#fbfbfb" stroke-width="1.6"/></svg>
        yourname@yourwebsite.com
      </li>
      <li class="contact__item">
        <svg class="contact__icon" viewBox="0 0 20 20"><circle cx="10" cy="10" r="9"/><g fill="none" stroke="#fbfbfb" stroke-width="1.2"><ellipse cx="10" cy="10" rx="4" ry="9"/><path d="M1 10h18M2.5 6h15M2.5 14h15"/></g></svg>
        www.yourwebsite.com
      </li>
      <li class="contact__address">Your Long Commercial or business address in 2 line</li>
    </ul>
  </section>
</body>
</html>
```